Quorvex - Automated robotic Inspection with AI need new business cards

We need a new design of our business cards. The company is focused on automated quality control at high speed with unmatched results. We have a logo but need a more forward leaning business card that shows that we are delivering cutting edge technology.

Contact Information for Business Card

Name
Position
Adress
Phone
Email
e.g.
Lena Holmqvist
Chief Financial Officer (CFO)

Quorvex Sweden AB
Bruksvägen 14, SE-175 43 JÄRFÄLLA, Sweden
Mobile: +46735 21 47 83 | Office: +46 8 61 94 27
www.quorvex-example.com

Font styles to use
Sans Serif

```html
<!DOCTYPE html>
<html lang="en">
<head>
<meta charset="utf-8">
<title>Quorvex Business Card</title>
<link href="https://fonts.googleapis.com/css2?family=Arimo:wght@400;700&display=swap" rel="stylesheet">
<style>
  :root {
    --stage: #e4e6e9;
    --brand-blue: #1c5a8c;
    --brand-blue-deep: #174c78;
    --ink: #2d2d2d;
    --rule: #b9b9b9;
    --paper: #ffffff;
    --white: #ffffff;
  }
  html, body {
    margin: 0;
    width: 1200px;
    height: 1015px;
    overflow: hidden;
    background: var(--stage);
    font-family: "Arimo", Arial, sans-serif;
  }
  .canvas { position: relative; width: 1200px; height: 1015px; }
  .card {
    position: absolute;
    width: 560px;
    height: 320px;
    box-shadow: 0 10px 24px rgba(0,0,0,.22);
    overflow: hidden;
  }
  /* Back side */
  .card-back { left: 80px; top: 140px; background: var(--brand-blue); }
  .gear-pattern {
    position: absolute; inset: 0;
    background: radial-gradient(circle at 50% 50%, #2168a0 0%, var(--brand-blue) 55%, var(--brand-blue-deep) 100%);
  }
  .back-wordmark {
    position: absolute; left: 0; right: 0; top: 146px;
    display: flex; justify-content: center; align-items: center; gap: 8px;
    color: var(--white); font-weight: 700; font-size: 20px; letter-spacing: 1px;
  }
  .back-wordmark .dot { width: 12px; height: 12px; border-radius: 50%; background: var(--white); }
  /* Front side */
  .card-front { left: 560px; top: 540px; background: var(--paper); }
  .front-wordmark {
    position: absolute; right: 36px; top: 58px;
    display: flex; align-items: center; gap: 14px;
    color: var(--brand-blue); font-weight: 700; font-size: 52px; letter-spacing: 2px;
  }
  .front-wordmark .dot { width: 36px; height: 36px; border-radius: 50%; background: var(--brand-blue); }
  .logo-rule { position: absolute; left: 250px; right: 20px; top: 142px; border-top: 1px solid var(--rule); }
  .person { position: absolute; left: 40px; top: 176px; width: 250px; }
  .person-name { margin: 0; color: var(--brand-blue); font-weight: 700; font-size: 19px; letter-spacing: .5px; text-transform: uppercase; }
  .person-title { margin: 3px 0 0; color: var(--ink); font-size: 14px; }
  .person-rule { margin: 9px 0 8px; border: 0; border-top: 1px solid var(--rule); width: 235px; }
  .contact-list { list-style: none; margin: 0; padding: 0; }
  .contact-list li { display: flex; align-items: center; gap: 9px; color: var(--ink); font-size: 13.5px; line-height: 19px; }
  .contact-list svg { width: 13px; height: 13px; fill: var(--brand-blue); flex: none; }
  .contact-list .accent { color: var(--brand-blue); }
  .company { position: absolute; right: 34px; top: 182px; text-align: right; color: var(--ink); font-size: 14px; line-height: 18px; }
  .company-name { margin: 0 0 2px; color: var(--brand-blue); font-weight: 700; font-size: 15px; }
  .company p { margin: 0; }
</style>
</head>
<body>
<main class="canvas">
  <section class="card card-back">
    <div class="gear-pattern" role="img" aria-label="Repeating pattern of embossed gear rings on blue"></div>
    <div class="back-wordmark"><span class="dot"></span>Quorvex</div>
  </section>

  <section class="card card-front">
    <div class="front-wordmark"><span class="dot"></span>QUORVEX</div>
    <div class="logo-rule"></div>

    <div class="person">
      <h1 class="person-name">Lena Holmqvist</h1>
      <p class="person-title">Chief Financial Officer (CFO)</p>
      <hr class="person-rule">
      <ul class="contact-list">
        <li><svg viewBox="0 0 16 16"><path d="M4 1h8a1 1 0 0 1 1 1v12a1 1 0 0 1-1 1H4a1 1 0 0 1-1-1V2a1 1 0 0 1 1-1zm1 2v9h6V3zm3 10a.8.8 0 1 0 0 1.6.8.8 0 0 0 0-1.6z"/></svg>+46735 21 47 83</li>
        <li><svg viewBox="0 0 16 16"><path d="M3.5 1.5l2.5 3-1.5 1.8c.8 1.8 2.3 3.3 4.2 4.2L10.5 9l3 2.5-1.5 2.8C6.5 14 2 9.5 1.8 3z"/></svg>+46 8 61 94 27</li>
        <li><svg viewBox="0 0 16 16"><path d="M1 3h14v10H1zm1.5 1.5v.3L8 9l5.5-4.2v-.3zm0 2.2v4.8h11V6.7L8 11z"/></svg>info@quorvex-example.com</li>
        <li><svg viewBox="0 0 16 16"><path d="M8 1a7 7 0 1 0 0 14A7 7 0 0 0 8 1zm-1 1.7V5H4.3A5.5 5.5 0 0 1 7 2.7zm2 0A5.5 5.5 0 0 1 11.7 5H9zM3.6 6.5H7v3H3.6a5.4 5.4 0 0 1 0-3zm5.4 0h3.4a5.4 5.4 0 0 1 0 3H9zM4.3 11H7v2.3A5.5 5.5 0 0 1 4.3 11zM9 11h2.7A5.5 5.5 0 0 1 9 13.3z"/></svg>www.<span class="accent">quorvex-example</span>.com</li>
      </ul>
    </div>

    <address class="company">
      <p class="company-name">Quorvex Sweden AB</p>
      <p>Bruksvägen 14, SE-175 43</p>
      <p>JÄRFÄLLA, Sweden</p>
    </address>
  </section>
</main>
</body>
</html>
```